Relay 84 Training is our company name. and instruction

We provide emergency medical training for CPR (Cardiopulmonary Resuscitation) /AED (Automated External Defibrillation) , BLS (Basic Life Support, First Aid, Bloodborne Pathogens
We travel to the client, give certified (NRS) Northfield Rescue Society (NRS) instruction for job/industry certification in the areas listed.
NRS Homeward Course noncertified instruction

Target Market(s)

Medical professionals, job required certification

Industry/Entity Type

Medical And Science

Contact Information for Business Card

Logo
Phone, email, address, website address, FB, Instagram

Font styles to use
Serif
Sans Serif

Colors
fff2fe
ff1b2f

Requirements
Must have
• Logo
Course taught: CPR (Cardiopulmonary Resuscitation)
AED (Automated External Defibrillation)
First Aid
BLS (Basic Life Support)
Bloodborne Pathogens
Offsite instruction - we come to you
Nice to have
• Red/Black scheme
Possible ecg/heart rhythm design
Should not have
• Cartoon images

```html
<!DOCTYPE html>
<html lang="en">
<head>
<meta charset="utf-8">
<title>Relay 84 Training – Business Card</title>
<link rel="stylesheet" href="https://fonts.googleapis.com/css2?family=Roboto:wght@400;500;700&display=swap">
<style>
  :root {
    --page: #ececee;
    --card: #2b2b2d;
    --red: #ef1c2b;
    --text: #ececec;
    --muted: #bdbdbd;
    --rule: #6a6a6a;
    --ghost: #3a3a3d;
  }
  * { box-sizing: border-box; margin: 0; padding: 0; }
  html, body { width: 1200px; height: 801px; overflow: hidden; }
  body {
    background: var(--page);
    font-family: "Roboto", Arial, sans-serif;
    display: flex;
    align-items: center;
    justify-content: center;
    gap: 48px;
  }
  .card {
    width: 540px;
    height: 309px;
    background: var(--card);
    border-bottom: 5px solid var(--red);
    border-left: 3px solid var(--red);
    box-shadow: 0 10px 24px rgba(0,0,0,.18);
    position: relative;
    color: var(--text);
  }
  /* Front */
  .card-front { display: flex; align-items: center; }
  .brand {
    width: 255px;
    display: flex;
    align-items: center;
    justify-content: center;
    gap: 12px;
  }
  .brand-dot { width: 22px; height: 22px; border-radius: 50%; background: var(--red); flex: none; }
  .brand-name { font-size: 22px; font-weight: 700; color: var(--text); white-space: nowrap; }
  .divider { width: 1px; height: 150px; background: var(--rule); }
  .contact { padding-left: 26px; font-size: 14px; line-height: 1.35; }
  .contact-name { color: var(--red); font-size: 21px; font-weight: 700; }
  .contact-role { font-size: 16px; margin-bottom: 10px; }
  .contact-address { margin-bottom: 10px; }
  .contact-list { list-style: none; }
  .contact-list li { display: flex; align-items: center; gap: 9px; }
  .contact-list svg { width: 12px; height: 12px; fill: none; stroke: var(--red); stroke-width: 2; }
  .accent { color: var(--red); }
  /* Back */
  .card-back {
    display: flex;
    flex-direction: column;
    align-items: center;
    justify-content: center;
    text-align: center;
  }
  .brand-ghost {
    font-size: 30px;
    font-weight: 700;
    color: var(--ghost);
    margin-bottom: 26px;
  }
  .courses-title { color: var(--red); font-size: 17px; font-weight: 700; margin-bottom: 4px; }
  .courses { font-size: 14.5px; line-height: 1.35; color: var(--text); }
  .bullet {
    display: inline-block; width: 8px; height: 8px; border-radius: 50%;
    background: var(--red); margin: 0 5px; vertical-align: middle;
  }
</style>
</head>
<body>
  <section class="card card-front">
    <div class="brand">
      <span class="brand-dot"></span>
      <span class="brand-name">Relay 84 Training</span>
    </div>
    <div class="divider"></div>
    <div class="contact">
      <div class="contact-name">Daniel Reyes</div>
      <div class="contact-role">Manager</div>
      <div class="contact-address">Your address, city<br>state, ZIP 0000</div>
      <ul class="contact-list">
        <li><svg viewBox="0 0 12 12"><path d="M2 1.5l2 .2.8 2.3-1.2 1a6 6 0 0 0 3.4 3.4l1-1.2 2.3.8.2 2A1 1 0 0 1 9.5 11 8.5 8.5 0 0 1 1 2.5a1 1 0 0 1 1-1z"/></svg>123-456-2100</li>
        <li><svg viewBox="0 0 12 12"><rect x="1" y="2.5" width="10" height="7"/><path d="M1 2.5l5 4 5-4"/></svg>youremail@relaymail.com</li>
        <li><svg viewBox="0 0 12 12"><circle cx="6" cy="6" r="5"/><path d="M1 6h10M6 1c2.5 3 2.5 7 0 10M6 1c-2.5 3-2.5 7 0 10"/></svg>www.<span class="accent">yourwebsite</span>.com</li>
      </ul>
    </div>
  </section>

  <section class="card card-back">
    <div class="brand-ghost">Relay 84 Training</div>
    <div class="courses-title">Course taught:</div>
    <p class="courses">
      CPR (Cardiopulmonary Resuscitation)<br>
      AED (Automated External Defibrillation)<span class="bullet"></span>First Aid<br>
      BLS (Basic Life Support)<span class="bullet"></span>Bloodborne Pathogens<br>
      Offsite instruction - we come to you
    </p>
  </section>
</body>
</html>
```